Flyer für KRV-Net.de
Zielgruppe
IT-Dienstleistungen
IT-Berater für Systemlösungen
siehe www.krv-net.de
Zielgruppe: Kleinunternehmen, Fachbereichsübergreifend
Aufgabenstellung
Erstellung eines kreativen Flyers
Größe des Flyers: doppelseitig, daher zweiseitig.

```html
<!DOCTYPE html>
<html lang="de">
<head>
<meta charset="utf-8">
<title>KRV-Net.de – Flyer Vorder- und Rückseite</title>
<link rel="stylesheet" href="https://fonts.googleapis.com/css2?family=Roboto+Condensed:wght@300;400&display=swap">
<style>
  :root{
    --brand:#176b97;
    --ink:#1d6b99;
    --paper:#ffffff;
    --stage:#eef1f3;
    --photo-a:#cfe0ec;
    --photo-b:#5d8fb3;
    --photo-c:#1f4d70;
  }
  *{box-sizing:border-box;margin:0;padding:0}
  html,body{width:1200px;height:848px;overflow:hidden}
  body{background:var(--stage);font-family:"Roboto Condensed","Arial Narrow",sans-serif;position:relative}

  .page{position:absolute;top:91px;width:470px;height:665px;background:var(--paper);box-shadow:0 6px 24px rgba(0,0,0,.12);overflow:hidden}
  .page--front{left:100px}
  .page--back{left:630px}

  /* Front */
  .hero-photo{position:absolute;left:24px;top:42px;width:424px;height:300px;
    background:linear-gradient(160deg,var(--photo-a) 0%,var(--photo-b) 55%,var(--photo-c) 100%)}
  .callout{position:absolute;right:30px;top:0;width:135px;height:124px;background:var(--brand);color:#fff;
    text-align:center;font-size:17px;line-height:26px;padding-top:22px;text-transform:uppercase}
  .service-band{position:absolute;left:24px;top:330px;width:424px;height:240px;background:var(--brand)}
  .question-badge{position:absolute;left:115px;top:246px;width:176px;height:176px;border-radius:50%;background:#fff;
    color:var(--ink);display:flex;align-items:center;justify-content:center;text-align:center;
    font-size:19px;line-height:25px;text-transform:uppercase}
  .service-list{position:absolute;left:24px;top:460px;width:424px;text-align:center;color:#fff;
    font-size:21px;line-height:29px;text-transform:uppercase}
  .brand-mark{position:absolute;right:34px;bottom:30px;display:flex;align-items:center;gap:14px;color:var(--ink)}
  .brand-mark__name{font-size:26px;line-height:30px;font-weight:400}
  .brand-dot{width:62px;height:62px;border-radius:50%;background:var(--brand)}

  /* Back */
  .service-panel{position:absolute;left:24px;top:24px;width:422px;height:490px;background:var(--brand);padding:22px 18px 0 18px}
  .service{display:flex;align-items:center;gap:14px;height:92px;color:#fff}
  .service__icon{flex:0 0 72px;width:72px;height:72px}
  .service__title{font-size:20px;line-height:23px;font-weight:400;text-transform:uppercase;margin-bottom:3px}
  .service__text{font-size:13.5px;line-height:17px;font-weight:300}
  .contact{position:absolute;right:110px;top:536px;text-align:right;color:var(--ink);font-size:15px;line-height:20px}
  .contact__name{font-size:17px}
  .back-dot{position:absolute;right:28px;top:548px;width:70px;height:70px;border-radius:50%;background:var(--brand)}
</style>
</head>
<body>

<section class="page page--front" aria-label="Flyer Vorderseite">
  <div class="hero-photo" role="img" aria-label="Foto eines Leitstands mit mehreren Monitoren in Blautönen"></div>
  <div class="callout">Rufen Sie an!<br>0511/48200170<br>INFO@KRV-NET.DE</div>
  <div class="service-band"></div>
  <div class="question-badge">Verzeifeln Sie?<br>Wir beraten<br>Sie gerne!</div>
  <p class="service-list">Netzwerk-Lösungen • IT-Sicherheit<br>Hardware • Mobile-Network<br>Homepage</p>
  <div class="brand-mark">
    <div class="brand-mark__name">KRV-Net.de</div>
    <div class="brand-dot" aria-hidden="true"></div>
  </div>
</section>

<section class="page page--back" aria-label="Flyer Rückseite">
  <div class="service-panel">
    <div class="service">
      <svg class="service__icon" viewBox="0 0 72 72" fill="none" stroke="#fff" stroke-width="3"><circle cx="36" cy="36" r="33"/><rect x="30" y="24" width="22" height="16" rx="1"/><path d="M41 40v6M35 47h12M20 26v8M26 26v8M18 34h10v4h-10zM23 38v8"/></svg>
      <div><h2 class="service__title">Netzwerk-Lösungen</h2><p class="service__text">Zusammen mit Ihnen finden und schaffen wir eine leistungsstarke, finanzierbare und für Sie abgestimmte IT-Infrastruktur.</p></div>
    </div>
    <div class="service">
      <svg class="service__icon" viewBox="0 0 72 72" fill="none" stroke="#fff" stroke-width="3"><circle cx="36" cy="36" r="33"/><path d="M36 18l14 5v11c0 10-7 16-14 20-7-4-14-10-14-20V23z" fill="#fff"/><path d="M36 27v13M36 44v3" stroke="#176b97" stroke-width="4"/></svg>
      <div><h2 class="service__title">IT-Sicherheit</h2><p class="service__text">Sie sind auf alle Risiken vorbereitet? Ein sicheres Konzept gibt Ihnen Sicherheit und spart Kosten.</p></div>
    </div>
    <div class="service">
      <svg class="service__icon" viewBox="0 0 72 72" fill="none" stroke="#fff" stroke-width="3"><circle cx="36" cy="36" r="33"/><rect x="22" y="22" width="28" height="28"/><rect x="29" y="29" width="14" height="14" fill="#fff"/><path d="M26 18v4M31 18v4M36 18v4M41 18v4M46 18v4M26 50v4M31 50v4M36 50v4M41 50v4M46 50v4M18 26h4M18 31h4M18 36h4M18 41h4M18 46h4M50 26h4M50 31h4M50 36h4M50 41h4M50 46h4" stroke-width="2"/></svg>
      <div><h2 class="service__title">Hardware</h2><p class="service__text">Eine leistungsstarke und qualitativ hochwertige Hardware ist die Grundlage jeder Arbeit. Wir zeigen Ihnen, dass diese auch finanzierbar ist.</p></div>
    </div>
    <div class="service">
      <svg class="service__icon" viewBox="0 0 72 72" fill="none" stroke="#fff" stroke-width="3"><circle cx="36" cy="36" r="33"/><rect x="27" y="29" width="18" height="27" rx="3"/><path d="M31 36h10M31 42h2M35 42h2M39 42h2M31 47h2M35 47h2M39 47h2M31 52h2M35 52h2M39 52h2" stroke-width="2.5"/><path d="M30 23a9 9 0 0 1 12 0M27 19a14 14 0 0 1 18 0" stroke-width="2.5"/></svg>
      <div><h2 class="service__title">Mobile-Network</h2><p class="service__text">Wir bereiten Sie für die mobile Welt der Zukunft vor und stehen Ihnen zur Seite.</p></div>
    </div>
    <div class="service">
      <svg class="service__icon" viewBox="0 0 72 72" fill="none" stroke="#fff" stroke-width="3"><circle cx="36" cy="36" r="33"/><path d="M28 20h14l9 9v23H28z"/><path d="M42 20v9h9"/><path d="M20 34l14 14-5 2 2-5z"/></svg>
      <div><h2 class="service__title">Homepage</h2><p class="service__text">Wir erstellen Ihre eigene Homepage. Dabei unterstützen wir Sie bei Ihren Ideen und setzen diese um.</p></div>
    </div>
  </div>
  <div class="contact">
    <div class="contact__name">Jonas Berger</div>
    IT-Berater für Systemlösungen • IT-Dienstleister<br>
    Ahornweg 14 • 30853 Langenhagen<br>
    Tel.:0511.48200170<br>
    info@krv-net.de • www.krv-net.de
  </div>
  <div class="back-dot" aria-hidden="true"></div>
</section>

</body>
</html>
```